Marta Quinlan Photography needs a unique, creative business card/logo design

I need a design for business cards/logo that is unique and creative in the industry. Simplicity is nice, so not too crowded. Something that will catch my customer's eye and remain in their memory. I am primarily a landscape photographer but will be soon may be branching into boudoir photography as well. I have attached my current card.

Industry/Entity Type

Business

Contact Information for Business Card

Marta Quinlan Photography
Phone: 0439 271 504
Email: MartaQuinlanPhotography@brivomail.net
Website: www.pagerly.net/MartaQuinlanPhotography.Aust

Logo Text

Marta Quinlan Photography

Requirements
Must have
• Contact Details on one side
Should not have
• pixelation

```html
<!DOCTYPE html>
<html lang="en">
<head>
<meta charset="utf-8">
<title>Marta Quinlan Photography – Business Card</title>
<link rel="stylesheet" href="https://fonts.googleapis.com/css2?family=Tinos&display=swap">
<style>
  :root {
    --backdrop: #6a6965;
    --card: #000000;
    --name: #c9c9c9;
    --tagline: #9a9a9a;
    --contact: #b8b8b8;
    --icon: #a8a8a8;
    --emblem: #bdbdbd;
    --emblem-faint: #242424;
    --name-faint: #262626;
  }
  html, body {
    margin: 0;
    width: 1200px;
    height: 910px;
    overflow: hidden;
    background: var(--backdrop);
    font-family: "Tinos", "Times New Roman", serif;
  }
  .card {
    position: absolute;
    top: 283px;
    width: 529px;
    height: 313px;
    background: var(--card);
  }
  .card--front { left: 58px; }
  .card--back { left: 610px; }

  .emblem {
    position: absolute;
    border-radius: 50%;
  }
  .card--front .emblem {
    left: 218px; top: 83px;
    width: 88px; height: 88px;
    background: var(--emblem);
  }

  .brand-name {
    position: absolute;
    margin: 0;
    font-weight: 400;
    letter-spacing: 3px;
    white-space: nowrap;
    color: var(--name);
    line-height: 1;
  }
  .brand-tagline {
    position: absolute;
    margin: 0;
    font-size: 12px;
    letter-spacing: 10px;
    color: var(--tagline);
    white-space: nowrap;
    line-height: 1;
  }
  .card--front .brand-name {
    left: 0; right: 0; top: 180px;
    text-align: center;
    font-size: 32px;
  }
  .card--front .brand-tagline {
    left: 10px; right: 0; top: 210px;
    text-align: center;
  }

  .card--back .brand-name {
    right: 32px; top: 40px;
    font-size: 32px;
  }
  .card--back .brand-tagline {
    right: 70px; top: 73px;
  }

  .contact-list {
    position: absolute;
    left: 226px; top: 104px;
    margin: 0; padding: 0;
    list-style: none;
  }
  .contact-item {
    display: flex;
    align-items: center;
    height: 25.5px;
    font-size: 11px;
    color: var(--contact);
    letter-spacing: 0.3px;
    white-space: nowrap;
  }
  .contact-item:first-child { letter-spacing: 1.5px; }
  .contact-icon {
    width: 12px; height: 12px;
    margin-right: 12px;
    fill: var(--icon);
    flex: none;
  }

  .card--back .emblem {
    left: 112px; top: 210px;
    width: 80px; height: 80px;
    background: var(--emblem-faint);
  }
  .faint-name {
    position: absolute;
    left: 200px; top: 242px;
    font-size: 18px;
    letter-spacing: 2px;
    color: var(--name-faint);
    white-space: nowrap;
  }
</style>
</head>
<body>

<section class="card card--front" aria-label="Card front">
  <div class="emblem" aria-hidden="true"></div>
  <h1 class="brand-name">MARTA QUINLAN</h1>
  <p class="brand-tagline">PHOTOGRAPHY</p>
</section>

<section class="card card--back" aria-label="Card back">
  <h2 class="brand-name">MARTA QUINLAN</h2>
  <p class="brand-tagline">PHOTOGRAPHY</p>

  <ul class="contact-list">
    <li class="contact-item">
      <svg class="contact-icon" viewBox="0 0 24 24" aria-hidden="true"><path d="M6.6 10.8a15.1 15.1 0 0 0 6.6 6.6l2.2-2.2a1 1 0 0 1 1-.25 11.4 11.4 0 0 0 3.6.57 1 1 0 0 1 1 1V20a1 1 0 0 1-1 1A17 17 0 0 1 3 4a1 1 0 0 1 1-1h3.5a1 1 0 0 1 1 1c0 1.25.2 2.45.57 3.57a1 1 0 0 1-.25 1z"/></svg>
      0439 271 504
    </li>
    <li class="contact-item">
      <svg class="contact-icon" viewBox="0 0 24 24" aria-hidden="true"><path d="M2 5h20v14H2z M3.5 6.5 12 13l8.5-6.5" fill="none" stroke="#a8a8a8" stroke-width="2"/><path d="M2 5h20L12 12.5z"/></svg>
      MartaQuinlanPhotography@brivomail.net
    </li>
    <li class="contact-item">
      <svg class="contact-icon" viewBox="0 0 24 24" aria-hidden="true"><circle cx="12" cy="12" r="10" fill="none" stroke="#a8a8a8" stroke-width="2"/><path d="M12 2a10 10 0 0 0 0 20c-3-3-3-17 0-20zM12 2c3 3 3 17 0 20a10 10 0 0 0 0-20zM2 12h20" fill="none" stroke="#a8a8a8" stroke-width="1.6"/></svg>
      www.pagerly.net/MartaQuinlanPhotography.Aust
    </li>
  </ul>

  <div class="emblem" aria-hidden="true"></div>
  <span class="faint-name" aria-hidden="true">MARTA QUINLAN</span>
</section>

</body>
</html>
```